TallonCryo Website - Biologics storage and handling

I would like a beginning design on a website for TallonCryo:

A Boston-based company dedicated to sourcing, storing, and supplying biologic materials of all kinds to the life sciences and scientific markets. From starting reagents, to basic and intermediate materials, to final synthesized and engineered products, we provide value throughout the biologics supply chain. TallonCryo provides backup, overflow, emergency, and stocking storage solutions to companies on a temporary or permanent basis. Life sciences companies can take advantage of the fact that the company is located in the middle of the Boston/Cambridge biotechnology corridor in order to have quick and efficient access to their cold chain materials. Out of state companies can leverage TallonCryo’s location for efficient distribution of materials to partner and client organizations. We also provide other value added services to organizations that do not have the local manpower, such as sourcing, supply, and distribution of materials.

The design should be mostly a white background with clean, linear, geometric colors added in according to the blue and orange color scheme represented in the corporate logo attached.

The website needs to communicate reliable service and provide the concept of a company dedicated to handling and providing client biological samples in a secure and efficient manner.

Some local competitors are:
1. Orlen BioServices: www.orlenbio-example.com
2. VaultiCore: www.vaulticore-example.com

From a design perspective, I like the Meridel Thera website:

www.merideltheraexample.com

Target Market(s)

Life sciences companies and other organizations

Industry/Entity Type

Biotechnology

Coding

Coded - Design and coding required

Number of Pages Required

5+ page

Font styles to use
Sans Serif

Colors
3176b5
0455a3
f37122

Requirements
Must have
• Tabs for pages:
About - Company information.
Platform - Inventory and sample management cloud platform; temperature profiling, logging, and reporting.
Services - Refrigeration and freezing services for biological samples, logistics services, sourcing services, courier services.
Updates - News, events, blog.
Login portal - Entry point for getting into platform. Maybe some freemium content here.
Nice to have
• Please be creative about website page sections, vibrant colors according to my established color scheme, and clean, linear, geometric shapes. I would like a white background with nice colors, clean lines and borders, and a very contemporary look. I want o
Should not have
• This is not a Business to Consumer business. This is a Business to Business enterprise. There should not be consumer oriented language. It is more about service and relationship management.

```html
<!DOCTYPE html>
<html lang="en">
<head>
<meta charset="utf-8">
<title>TallonCryo — Biologics Storage and Handling</title>
<link href="https://fonts.googleapis.com/css2?family=Questrial&family=Roboto:wght@400;500&family=Lato:wght@400&display=swap" rel="stylesheet">
<style>
:root{
  --orange:#e46c0c;
  --orange-deep:#7a3306;
  --blue:#3176b5;
  --blue-deep:#0a4a92;
  --purple:#5a2c70;
  --purple-light:#8a4497;
  --teal:#1f6f8b;
  --ink:#1c1c1c;
  --text:#4a4a4a;
  --grey-bg:#f4f4f4;
  --logo-grey:#6b6b6b;
  --white:#ffffff;
}
*{margin:0;padding:0;box-sizing:border-box}
html,body{width:1200px;height:2741px;overflow:hidden;background:var(--white)}
body{position:relative;font-family:'Lato',sans-serif;color:var(--text)}
.display{font-family:'Questrial',sans-serif;text-transform:uppercase;letter-spacing:1px}

/* hero */
.hero{position:absolute;left:0;top:0;width:1200px;height:600px;overflow:hidden}
.hero-photo{position:absolute;inset:0;background:linear-gradient(100deg,#4f86c2 0%,#7fa6cf 40%,#b9a9a8 65%,#e0a06e 100%)}
.site-header{position:absolute;left:0;top:0;width:1200px;height:99px;border-bottom:1px solid rgba(255,255,255,.45)}
.brand{position:absolute;left:110px;top:64px;display:flex;align-items:center;gap:10px;font-family:'Questrial',sans-serif;font-size:24px;line-height:28px;color:var(--white);letter-spacing:1px}
.brand-square{width:14px;height:14px;background:var(--orange)}
.contact-bar{position:absolute;left:812px;top:15px;display:flex;align-items:center;gap:8px;font-family:'Roboto',sans-serif;font-size:18px;line-height:26px;color:var(--white);white-space:nowrap}
.login{position:absolute;left:991px;top:10px;width:97px;height:36px;border-radius:18px;background:var(--orange);color:var(--white);font-family:'Roboto',sans-serif;font-size:17px;text-align:center;line-height:36px}
.main-nav{position:absolute;right:112px;top:62px;display:flex;gap:40px;font-family:'Roboto',sans-serif;font-size:16px;color:var(--white)}
.main-nav a{position:relative;height:37px;color:inherit;text-decoration:none}
.main-nav a.active{color:var(--orange)}
.main-nav a.active::after{content:"";position:absolute;left:-4px;right:-4px;bottom:0;height:2px;background:var(--orange)}
.hero-title{position:absolute;left:0;top:268px;width:1200px;text-align:center;font-size:26px;line-height:40px;color:var(--white);font-weight:400}
.hero-btn{position:absolute;left:520px;top:364px;width:161px;height:43px;border:2px solid var(--white);border-radius:22px;color:var(--white);font-family:'Roboto',sans-serif;font-size:16px;text-align:center;line-height:39px}
.hero-arrow{position:absolute;top:322px}
.dots{position:absolute;left:569px;top:549px;display:flex;gap:7px}
.dots span{width:10px;height:10px;border-radius:50%;background:rgba(255,255,255,.45)}
.dots span.on{background:var(--white)}

/* welcome */
.welcome{position:absolute;left:0;top:600px;width:1200px;height:380px;text-align:center}
.welcome-rule{position:absolute;left:575px;top:86px;width:50px;height:2px;background:var(--teal)}
.welcome h1{position:absolute;left:0;top:100px;width:1200px;font-weight:400;font-size:36px;color:var(--ink)}
.welcome p{position:absolute;left:155px;top:150px;width:890px;font-size:14px;line-height:28.3px;color:var(--text)}

/* feature bands */
.band{position:absolute;left:0;width:1200px;height:424px;overflow:hidden;color:var(--white)}
.band-art{position:absolute;top:0;height:100%}
.band h2{position:absolute;left:109px;font-weight:400;font-size:37px;line-height:48px}
.band .more{position:absolute;left:109px;font-family:'Roboto',sans-serif;font-weight:500;font-size:16.5px;text-transform:uppercase;display:flex;align-items:center;gap:4px}
.band-platform{top:980px;background:var(--orange)}
.band-platform .band-art{left:909px;width:291px;background:linear-gradient(115deg,rgba(122,51,6,.2) 0%,rgba(122,51,6,.75) 45%,var(--orange-deep) 100%)}
.band-services{top:1404px;background:linear-gradient(120deg,var(--purple) 0%,#4b2b68 40%,var(--purple-light) 75%,#6a2f78 100%)}
.band-services .band-art{left:0;width:1200px;background:linear-gradient(60deg,rgba(255,255,255,0) 30%,rgba(255,255,255,.06) 60%,rgba(0,0,0,.08) 100%)}
.band-updates{top:1828px;background:var(--blue)}
.band-updates .band-art{left:909px;width:291px;background:linear-gradient(115deg,rgba(10,74,146,.2) 0%,rgba(10,74,146,.8) 45%,var(--blue-deep) 100%)}
.band h2{top:138px}
.band .more{top:262px}
.band-services h2{top:140px}.band-services .more{top:260px}
.band-updates h2{top:140px}.band-updates .more{top:260px}

/* partners */
.partners{position:absolute;left:0;top:2253px;width:1200px;height:237px;background:var(--grey-bg)}
.partner-list{position:absolute;left:118px;top:98px;width:964px;display:flex;justify-content:space-between;align-items:center}
.partner{font-family:'Roboto',sans-serif;font-weight:500;font-size:28px;color:var(--logo-grey);display:flex;align-items:center;gap:8px}
.partner-mark{width:20px;height:20px;border-radius:50%;background:var(--logo-grey)}
.partner-arrow{position:absolute;top:110px}

/* footer */
.site-footer{position:absolute;left:0;top:2490px;width:1200px;height:251px}
.footer-nav{position:absolute;left:0;top:52px;width:1200px;display:flex;justify-content:center;gap:24px;font-family:'Roboto',sans-serif;font-weight:500;font-size:15.5px;color:var(--ink)}
.footer-nav .sep{font-weight:400}
.social{position:absolute;left:527px;top:105px;display:flex;gap:9px}
.social span{width:43px;height:43px;border:1.5px solid var(--ink);border-radius:50%;display:flex;align-items:center;justify-content:center}
.footer-rule{position:absolute;left:111px;top:184px;width:977px;height:1px;background:#d8d8d8}
.copyright{position:absolute;left:0;top:210px;width:1200px;text-align:center;font-size:13px;color:var(--ink)}
</style>
</head>
<body>

<section class="hero">
  <div class="hero-photo" role="img" aria-label="Scientists in lab coats working at laboratory instruments, tinted blue to orange with a faint hexagon overlay"></div>

  <header class="site-header">
    <div class="brand"><span class="brand-square"></span>TallonCryo</div>
    <div class="contact-bar">
      <svg width="26" height="26" viewBox="0 0 26 26" fill="none" stroke="#fff" stroke-width="1.4"><circle cx="13" cy="13" r="12"/><path d="M9 7.5l2 3-1.3 1.3a8 8 0 0 0 4.5 4.5L15.5 15l3 2-1.3 2.2c-4.6-.3-9.1-4.8-9.4-9.4z"/></svg>
      800 555 0142
    </div>
    <div class="login">LOGIN</div>
    <nav class="main-nav">
      <a class="active">Home</a><a>About</a><a>Platfrom</a><a>Service</a><a>Updates</a><a>Contact</a>
    </nav>
  </header>

  <h2 class="hero-title display">Sourcing, Storing, and Supplying<br>Biologic Materials</h2>
  <div class="hero-btn">GET STARTED</div>

  <svg class="hero-arrow" style="left:72px" width="20" height="40" viewBox="0 0 20 40"><path d="M18 2L2 20l16 18" fill="none" stroke="#fff" stroke-width="1.6"/></svg>
  <svg class="hero-arrow" style="left:1110px" width="20" height="40" viewBox="0 0 20 40"><path d="M2 2l16 18L2 38" fill="none" stroke="#fff" stroke-width="1.6"/></svg>

  <div class="dots"><span class="on"></span><span></span><span></span><span></span></div>
</section>

<section class="welcome">
  <div class="welcome-rule"></div>
  <h1 class="display">Welcome to Tallon Cryo</h1>
  <p>TallonCryo is dedicated to sourcing, storing, and supplying biologic materials of all kinds to the life sciences and scientific markets. From starting reagents, to basic and intermediate materials, to final synthesized and engineered products, we provide value throughout the biologics supply chain. TallonCryo provides backup, overflow, emergency, and stocking storage solutions to companies on a temporary or permanent basis. Life sciences companies can take advantage of the fact that the company is located in the middle of the Boston/Cambridge biotechnology corridor in order to have quick and efficient access to their cold chain materials...</p>
</section>

<section class="band band-platform">
  <div class="band-art" role="img" aria-label="Dark orange geometric hexagon pattern"></div>
  <h2 class="display">Inventory and Sample<br>Management Cloud Platform</h2>
  <div class="more">Discover the Platform
    <svg width="16" height="10" viewBox="0 0 16 10"><path d="M0 5h12M9 1l4 4-4 4" fill="none" stroke="#fff" stroke-width="2"/></svg></div>
</section>

<section class="band band-services">
  <div class="band-art" role="img" aria-label="Purple and violet faceted geometric pattern"></div>
  <h2 class="display">Refrigeration and Freezing<br>Services for Biological Samples</h2>
  <div class="more">See All Services
    <svg width="16" height="10" viewBox="0 0 16 10"><path d="M0 5h12M9 1l4 4-4 4" fill="none" stroke="#fff" stroke-width="2"/></svg></div>
</section>

<section class="band band-updates">
  <div class="band-art" role="img" aria-label="Deep blue geometric hexagon pattern"></div>
  <h2 class="display">Refrigeration and Freezing<br>Services for Biological Samples</h2>
  <div class="more">View Our Updates
    <svg width="16" height="10" viewBox="0 0 16 10"><path d="M0 5h12M9 1l4 4-4 4" fill="none" stroke="#fff" stroke-width="2"/></svg></div>
</section>

<section class="partners">
  <svg class="partner-arrow" style="left:86px" width="14" height="26" viewBox="0 0 14 26"><path d="M12 1L2 13l10 12" fill="none" stroke="#555" stroke-width="1.5"/></svg>
  <div class="partner-list">
    <div class="partner"><span class="partner-mark"></span>Kestrel Dx</div>
    <div class="partner">Norvale Bio</div>
    <div class="partner">Quillon</div>
    <div class="partner">Hexmoor Bio</div>
    <div class="partner">Tarnwell Labs</div>
  </div>
  <svg class="partner-arrow" style="left:1100px" width="14" height="26" viewBox="0 0 14 26"><path d="M2 1l10 12L2 25" fill="none" stroke="#555" stroke-width="1.5"/></svg>
</section>

<footer class="site-footer">
  <nav class="footer-nav">
    <span>Home</span><span class="sep">|</span><span>About</span><span class="sep">|</span><span>Platfrom</span><span class="sep">|</span><span>Service</span><span class="sep">|</span><span>Updates</span><span class="sep">|</span><span>Contact</span>
  </nav>
  <div class="social" aria-label="Contact links">
    <span aria-label="Email"><svg width="18" height="14" viewBox="0 0 18 14" fill="none" stroke="#1c1c1c" stroke-width="1.8"><rect x="1" y="1" width="16" height="12" rx="1"/><path d="M1 2l8 6 8-6"/></svg></span>
    <span aria-label="Chat"><svg width="18" height="16" viewBox="0 0 18 16" fill="#1c1c1c"><path d="M2 1h14a1 1 0 0 1 1 1v9a1 1 0 0 1-1 1H7l-4 3v-3H2a1 1 0 0 1-1-1V2a1 1 0 0 1 1-1z"/></svg></span>
    <span aria-label="Location"><svg width="14" height="18" viewBox="0 0 14 18" fill="#1c1c1c"><path d="M7 0a7 7 0 0 1 7 7c0 5-7 11-7 11S0 12 0 7a7 7 0 0 1 7-7zm0 4a3 3 0 1 0 0 6 3 3 0 0 0 0-6z"/></svg></span>
  </div>
  <div class="footer-rule"></div>
  <p class="copyright">© Copyright 2020. All Rights Reserved. Terms and Conditions | Privacy Policy</p>
</footer>

</body>
</html>
```